Phone Repair Business Card

I need a business card for my mobile phone/ smart phone and tablet repair business based in New Zealand. My business name is "T.K. Repairs". I would like to see a designer make a modern phone related business card, which could incorporate something to do with the Vorlan Zeltox as this is our main repaired product. i like the dark Grey and lime green colours

```html
<!DOCTYPE html>
<html lang="en">
<head>
<meta charset="utf-8">
<title>TK Repair – Business Card</title>
<link rel="stylesheet" href="https://fonts.googleapis.com/css2?family=Arimo:wght@400&display=swap">
<style>
  :root {
    --lime: #9dcf6a;
    --screen: #e5e7e6;
    --ink: #5a5055;
    --white: #ffffff;
    --speaker: #4a4a4a;
    --lens: #0c0c0c;
    --page: #ffffff;
  }
  * { margin: 0; padding: 0; box-sizing: border-box; }
  html, body {
    width: 1200px; height: 961px; overflow: hidden;
    background: var(--page);
    font-family: "Arimo", Arial, sans-serif;
  }
  .stage {
    position: relative;
    width: 1124px; height: 900px;
    transform: scale(1.0676); transform-origin: 0 0;
  }
  .card {
    position: absolute; top: 0;
    width: 528px; height: 899px;
    background: var(--lime);
  }
  .card--front { left: 0; }
  .card--back { left: 596px; }

  .device-decor { position: absolute; inset: 0; }

  .screen {
    position: absolute; left: 82px; top: 82px;
    width: 364px; height: 736px;
    background: var(--screen);
    border: 2px solid var(--white);
    box-shadow: 0 0 14px 8px rgba(255,255,255,.75), 0 0 34px 18px rgba(255,255,255,.35);
    color: var(--ink);
  }
  .brand-name {
    position: absolute; left: 26px; top: 14px;
    width: 310px; text-align: center;
    font-size: 52px; font-weight: 400; line-height: 1.2;
    padding-bottom: 2px;
    border-bottom: 2px solid var(--ink);
  }
  .contact { position: absolute; left: 30px; font-size: 28px; line-height: 37px; }
  .contact--name { top: 154px; font-size: 32px; }
  .contact--title { top: 212px; }
  .contact--address { top: 322px; }
  .contact--reach { top: 508px; }
  .contact--web { top: 658px; }

  .back-art { position: absolute; inset: 0; }
  .back-title { font-size: 50px; fill: var(--white); }
  .back-tagline { font-size: 20px; fill: var(--white); }
</style>
</head>
<body>
<main class="stage">
  <section class="card card--front">
    <svg class="device-decor" width="528" height="899" viewBox="0 0 528 899" aria-hidden="true">
      <circle cx="268" cy="21" r="3" fill="var(--white)"/>
      <rect x="236" y="35" width="64" height="10" rx="5" fill="var(--speaker)"/>
      <circle cx="264" cy="859" r="29" fill="none" stroke="var(--white)" stroke-width="3"/>
      <rect x="252" y="847" width="24" height="24" rx="2" fill="none" stroke="var(--white)" stroke-width="3"/>
    </svg>
    <div class="screen">
      <h1 class="brand-name">TK Repair</h1>
      <p class="contact contact--name">Employee Name</p>
      <p class="contact contact--title">Title</p>
      <p class="contact contact--address">Address 1<br>Address 2<br>City, State Zip</p>
      <p class="contact contact--reach">Phone #<br>Email</p>
      <p class="contact contact--web">website</p>
    </div>
  </section>

  <section class="card card--back">
    <svg class="back-art" width="528" height="899" viewBox="0 0 528 899">
      <circle class="camera-lens" cx="467" cy="62" r="24" fill="var(--lens)"/>
      <circle cx="467" cy="62" r="19" fill="none" stroke="#555" stroke-width="1.5"/>
      <text class="back-title" transform="translate(295 451) rotate(90)" text-anchor="middle">TK Repair</text>
      <text class="back-tagline" transform="translate(234 450) rotate(90)" text-anchor="middle">We fix all brands of smartphones and tablets</text>
    </svg>
  </section>
</main>
</body>
</html>
```